Modern Venture Capital website

Design a modern website for a venture capital firm. This website should be modern and beautiful and be on par with other Venture Capital websites. I have a logo and a hero video I'd like to use. Link to hero video: https://files.vantoria.example/f/9Xk2Lm7qPz4Rt8Wb3Nc6Hd5Jy1Gs0Ve/view?ref=share_link

Preference will be given to the best design that combines design with the best images and digital content. That means no generic free stock videos 😅

I currently built a wix website to give you an idea of what content needs to be on the website. Depending on your design it can be 3 pages, or one long page. I will leave it up to you.

WEBSITE: https://brelmor58204.pagecraftly.example/my-site-4

Target Market(s)

Mid-career professionals, individuals interested in Venture Capital

Industry/Entity Type

Finance, venture capital, startups

Requirements
Must have
• must use the hero video I have and must use my logo. Must use high quality images that matches the website design - no generic stock images

```html
<!DOCTYPE html>
<html lang="en">
<head>
<meta charset="utf-8">
<title>Moonlit Ventures — Venture Capital for the Late Night Hustlers</title>
<link rel="stylesheet" href="https://fonts.googleapis.com/css2?family=Outfit:wght@300;400;500;600;700;800&display=swap">
<style>
:root{
  --bg:#020202;
  --ink:#ffffff;
  --muted:#b9b9b9;
  --dim:#8a8a8a;
  --orange:#ff5a0a;
  --orange-soft:#ff7a2e;
  --card:#141414;
  --card-line:#2a2a2a;
  --field:#ffffff;
}
*{box-sizing:border-box;margin:0;padding:0}
html,body{width:1200px;height:4458px;overflow:hidden;background:var(--bg)}
body{position:relative;font-family:'Outfit',sans-serif;color:var(--ink)}
.abs{position:absolute}
.accent{color:var(--orange)}
.btn{position:absolute;display:flex;align-items:center;justify-content:center;gap:6px;background:var(--orange);color:#fff;border-radius:30px;font-weight:600;font-size:15px;text-decoration:none}
.btn-outline{background:transparent;border:2px solid var(--orange)}
.vline{position:absolute;width:2px;background:linear-gradient(#ff5a0a00,var(--orange))}
.vline::after{content:"";position:absolute;bottom:-4px;left:-3px;width:8px;height:8px;border-radius:50%;background:var(--orange)}
.sec-title{position:absolute;left:0;width:1200px;text-align:center;font-weight:600;font-size:40px;letter-spacing:.5px}

/* hero */
.hero-scene{position:absolute;left:0;top:0;width:1200px;height:740px;
  background:radial-gradient(ellipse 760px 150px at 600px 400px,#3b2d1f,transparent 70%),
  radial-gradient(ellipse 420px 90px at 560px 330px,#2a2018,transparent 75%),
  linear-gradient(#050505 0,#0d0d10 30%,#1a1510 55%,#0a0806 80%,#020202 100%)}
.nav-logo{left:121px;top:22px;line-height:1}
.nav-logo .word{font-size:48px;font-weight:800;letter-spacing:-1px}
.nav-logo .sub{font-size:15px;font-weight:700;letter-spacing:5px;margin-top:-2px}
.nav-link{position:absolute;top:46px;font-size:14px;color:#e8e8e8}
.hero-title{left:121px;top:472px;font-size:56px;font-weight:600;line-height:62px;letter-spacing:.5px}
.hero-title .accent{font-weight:400}
.hero-sub{left:123px;top:612px;font-size:23px;font-weight:400}

/* features */
.intro{left:140px;top:898px;width:920px;text-align:center;font-size:18px;line-height:31px;color:var(--muted);font-weight:300}
.wave{position:absolute;left:0;width:1200px;
  background:radial-gradient(ellipse 620px 90px at 60% 50%,#4a3522aa,transparent 70%),
  radial-gradient(ellipse 500px 70px at 25% 60%,#3a2a1a88,transparent 70%)}
.feature{position:absolute;width:240px;text-align:center}
.ring{width:88px;height:88px;margin:0 auto;border-radius:50%;border:3px solid var(--orange);display:flex;align-items:center;justify-content:center;box-shadow:-4px 4px 0 0 var(--orange) inset}
.ring svg{width:44px;height:44px}
.feature h3{font-size:18px;font-weight:600;line-height:24px;margin-top:14px}
.feature p{font-size:11.5px;line-height:19px;color:#d2d2d2;margin-top:8px;font-weight:300}
.drop{position:absolute;border-left:2px dotted #888;width:0}
.drop::after{content:"";position:absolute;bottom:-12px;left:-8px;width:14px;height:14px;border-radius:50%;border:2px solid #fff;background:#000}

/* stats */
.stat{position:absolute;width:218px;height:134px;background:var(--card);border:1px solid var(--card-line);border-radius:4px;padding:22px 0 0 30px}
.stat::before{content:"";position:absolute;left:0;top:24px;width:3px;height:46px;background:var(--orange)}
.stat b{display:block;font-size:40px;font-weight:600;line-height:44px}
.stat span{font-size:17px;color:var(--dim);line-height:24px;font-weight:300}
.founders h2{font-size:39px;font-weight:600;line-height:52px}
.founders p{font-size:17px;line-height:26px;color:var(--muted);font-weight:300}

/* partners */
.city{position:absolute;left:0;top:2390px;width:1200px;height:330px;
  background:linear-gradient(90deg,transparent 0,transparent 78%,#1e2a3a 82%,#24303f 90%,#0c0c10 96%),
  linear-gradient(#020202 0,#0b0d14 40%,#1d1a22 65%,#2d2014 80%,#020202 100%)}
.partner{position:absolute;top:2449px;width:225px;height:97px;background:#0b0b0b;border:1px solid #3a3a3a;display:flex;align-items:center;justify-content:center}
.partner i{display:block;width:120px;height:22px;border-radius:4px;background:#5a5a5a}

.better h2{font-size:39px;font-weight:600;line-height:52px}
.node{position:absolute;width:90px;height:90px;margin:-45px 0 0 -45px;border-radius:50%;border:3px solid var(--orange);background:#050505;display:flex;align-items:center;justify-content:center}
.node svg{width:44px;height:44px}
.node-label{position:absolute;width:240px;text-align:center;font-size:16px;font-weight:600;line-height:23px}

/* contact */
.contact-box{position:absolute;left:170px;top:3507px;width:857px;height:477px;border:1px solid #3a3a3a;border-radius:18px;
  background:radial-gradient(ellipse 520px 320px at 95% 100%,#7a2c08cc,transparent 70%),#050505}
.field{position:absolute;background:var(--field);color:#333;font-size:12.5px;display:flex;align-items:center;gap:6px;padding-left:16px;border:none}
.field svg{width:12px;height:12px;fill:#999}
.field.msg{align-items:flex-start;padding-top:14px}

/* footer */
.foot-h{position:absolute;top:4085px;font-size:19px;font-weight:600}
.foot-h::after{content:"";position:absolute;left:0;top:33px;width:173px;height:1px;background:#444}
.foot-l{position:absolute;font-size:15px;color:#d4d4d4;font-weight:300}
.social{position:absolute;top:4176px;width:22px;height:22px;border-radius:50%;background:#fff}
.copyright{position:absolute;left:0;top:4394px;width:1200px;text-align:center;font-size:13px;color:#777}
</style>
</head>
<body>

<!-- HERO -->
<div class="hero-scene" role="img" aria-label="Hero video: night city skyline under a moonlit sky"></div>
<div class="abs nav-logo"><div class="word">Moonlit</div><div class="sub">VENTURES</div></div>
<a class="nav-link" style="left:530px">Home</a>
<a class="nav-link" style="left:630px">Join VC</a>
<a class="nav-link" style="left:737px">Startups</a>
<a class="nav-link" style="left:851px">Login</a>
<a class="btn btn-outline" style="left:946px;top:36px;width:140px;height:39px;font-size:14px;color:var(--orange)">Get Started ↗</a>

<h1 class="abs hero-title">Venture Capital for the<br><span class="accent">Late Night Hustlers</span></h1>
<p class="abs hero-sub">Become a Venture Capital Investor</p>
<a class="btn" style="left:916px;top:546px;width:161px;height:38px">Learn More →</a>

<div class="vline" style="left:600px;top:672px;height:81px"></div>

<!-- BECOME A VC -->
<h2 class="sec-title" style="top:810px">Become a <span class="accent">VC</span></h2>
<p class="abs intro">At Moonlit Ventures, we're opening the doors to a new kind of investor, mid-career professionals and aspiring VCs who want real skin in the game, not just exposure from the sidelines.</p>

<div class="wave" style="top:1340px;height:290px" role="img" aria-label="Glowing particle wave landscape"></div>

<div class="feature" style="left:64px;top:1070px">
  <div class="ring"><svg viewBox="0 0 44 44" fill="none" stroke="#fff" stroke-width="2"><path d="M6 34h10l8-4h10M10 26l8-8 6 5 10-11M30 12h5v5"/></svg></div>
  <h3>Hands on<br>VC Work</h3>
  <p>Each Moonlit Investor can actively be involved in sourcing, evaluating, and making key investment decisions as little or as much as they want</p>
</div>
<div class="feature" style="left:325px;top:1151px">
  <div class="ring"><svg viewBox="0 0 44 44" fill="none" stroke="#fff" stroke-width="2"><circle cx="22" cy="12" r="5"/><circle cx="12" cy="22" r="4"/><circle cx="32" cy="22" r="4"/><path d="M6 34c0-5 4-8 8-8M38 34c0-5-4-8-8-8M14 36c0-6 4-10 8-10s8 4 8 10z"/></svg></div>
  <h3>Earn Carry and Put<br>Your Name on<br>an Investment</h3>
  <p>Earn carry interest based on the level of your involvement on each deal.</p>
</div>
<div class="feature" style="left:611px;top:1037px">
  <div class="ring"><svg viewBox="0 0 44 44" fill="none" stroke="#fff" stroke-width="2"><rect x="10" y="8" width="24" height="18" rx="2"/><path d="M15 22v-4M20 22v-8M25 22v-6M30 22v-10M8 36l6-6h10l6 4"/></svg></div>
  <h3>Meaningful Opportunities<br>to develop your career<br>in Venture Capital</h3>
  <p>Moonlit Investors, depending on the level of commitment and involvement, can work at our fund as Partners, Principals, Senior Associates, Associates and Venture Partners.</p>
</div>
<div class="feature" style="left:878px;top:1113px">
  <div class="ring"><svg viewBox="0 0 44 44" fill="none" stroke="#fff" stroke-width="2"><circle cx="22" cy="22" r="5"/><circle cx="10" cy="10" r="3"/><circle cx="34" cy="10" r="3"/><circle cx="10" cy="34" r="3"/><circle cx="34" cy="34" r="3"/><path d="M12 12l6 6M32 12l-6 6M12 32l6-6M32 32l-6-6"/></svg></div>
  <h3>Join a community<br>of Hustlers</h3>
  <p>Network with likeminded investors, aspiring investors and limited partners.</p>
</div>
<div class="drop" style="left:183px;top:1348px;height:135px"></div>
<div class="drop" style="left:444px;top:1400px;height:135px"></div>
<div class="drop" style="left:730px;top:1370px;height:135px"></div>
<div class="drop" style="left:1009px;top:1355px;height:72px"></div>

<!-- STATS -->
<svg class="abs" style="left:0;top:1660px" width="1200" height="600" viewBox="0 0 1200 600" role="img" aria-label="Rising market line">
  <defs><linearGradient id="chartFill" x1="0" y1="0" x2="0" y2="1"><stop offset="0" stop-color="#1b2a3a" stop-opacity=".6"/><stop offset="1" stop-color="#020202" stop-opacity="0"/></linearGradient></defs>
  <path d="M0 590 L40 540 L80 560 L130 520 L200 530 L260 470 L330 440 L420 350 L500 300 L600 260 L700 200 L800 160 L900 120 L1000 110 L1080 60 L1140 20 L1200 30 V600 H0Z" fill="url(#chartFill)"/>
  <path d="M0 590 L40 540 L80 560 L130 520 L200 530 L260 470 L330 440" stroke="#4a6a8a" stroke-width="1.5" fill="none"/>
  <path d="M1030 100 L1080 60 L1140 20 L1200 30" stroke="#4a6a8a" stroke-width="1.5" fill="none"/>
</svg>
<div class="stat" style="left:107px;top:1796px"><b>14</b><span>Pre-Seed /<br>Seed Investments</span></div>
<div class="stat" style="left:107px;top:1954px"><b>50K</b><span>Check Size</span></div>
<div class="stat" style="left:341px;top:1722px"><b>20%</b><span>Carried Interest</span></div>
<div class="stat" style="left:341px;top:1871px"><b>2.5%</b><span>Management Fee</span></div>
<div class="stat" style="left:341px;top:2021px"><b>1M</b><span>Fund Size</span></div>

<div class="abs founders" style="left:632px;top:1726px;width:515px">
  <h2>Simplifying Success<br><span class="accent">for Founders</span></h2>
  <p style="margin-top:24px">Our strength lies in our network. Our LPs and operating partners are all mid-to-senior level executives in their industries. They bring real-world corporate experience, offering strategic insights and operational support to help our portfolio companies scale efficiently.</p>
  <p style="margin-top:28px">We cut through the noise and get to the core of your business fast. If we love what you're building, we'll move. If not, we'll tell you quickly and respectfully. That lets you make</p>
</div>
<div class="abs" style="left:1026px;top:1816px;width:174px;height:2px;background:var(--orange)"></div>
<div class="abs" style="left:1022px;top:1813px;width:8px;height:8px;border-radius:50%;background:var(--orange)"></div>
<a class="btn" style="left:632px;top:2115px;width:151px;height:36px;font-size:14px">Learn More →</a>

<div class="vline" style="left:600px;top:2190px;height:135px"></div>

<!-- PARTNERS -->
<div class="city" role="img" aria-label="Night city skyline with glass tower on the right"></div>
<h2 class="sec-title" style="top:2340px">Our <span class="accent">Partners</span></h2>
<div class="partner" style="left:123px"><i></i></div>
<div class="partner" style="left:365px"><i></i></div>
<div class="partner" style="left:610px"><i></i></div>
<div class="partner" style="left:854px"><i></i></div>

<!-- BETTER WAY -->
<div class="abs" style="left:0;top:2756px;width:118px;height:2px;background:var(--orange)"></div>
<div class="abs" style="left:120px;top:2753px;width:8px;height:8px;border-radius:50%;background:var(--orange)"></div>
<div class="abs better" style="left:151px;top:2728px"><h2>A better way to be part<br>of <span class="accent">Venture Capital</span></h2></div>
<p class="abs" style="left:665px;top:2747px;width:440px;font-size:17px;line-height:26px;color:var(--muted);font-weight:300">Backing bold founders and connecting passionate investors before the world catches on.</p>

<div class="wave" style="top:3190px;height:220px" role="img" aria-label="Glowing particle wave landscape"></div>
<svg class="abs" style="left:0;top:2800px" width="1200" height="400" viewBox="0 2800 1200 400">
  <polyline points="107,3131 229,3053 315,3024 521,3124 757,2970 866,3031 1020,2915 1091,2868" fill="none" stroke="#bbb" stroke-width="1.5"/>
</svg>
<div class="node" style="left:229px;top:3053px"><svg viewBox="0 0 44 44" fill="none" stroke="#fff" stroke-width="2"><rect x="10" y="8" width="16" height="26"/><path d="M14 14h3M20 14h3M14 20h3M20 20h3M14 26h3M20 26h3"/><circle cx="32" cy="28" r="5"/><path d="M26 38c0-4 3-5 6-5s6 1 6 5"/></svg></div>
<div class="node" style="left:521px;top:3124px"><svg viewBox="0 0 44 44" fill="none" stroke="#fff" stroke-width="2"><path d="M6 36h8v-8h8v-8h8v-8h8M26 8l6-4 2 6"/></svg></div>
<div class="node" style="left:757px;top:2970px"><svg viewBox="0 0 44 44" fill="none" stroke="#fff" stroke-width="2"><path d="M8 34l8-10 6 6 14-16M12 34v-6M18 34v-8M24 34v-4M30 34v-10"/></svg></div>
<div class="node" style="left:1020px;top:2915px"><svg viewBox="0 0 44 44" fill="none" stroke="#fff" stroke-width="2"><circle cx="28" cy="14" r="7"/><path d="M28 10v8M6 36l6-6h10l8-4 6-2"/></svg></div>
<div class="node-label" style="left:109px;top:2930px">No previous Venture<br>Capital experience<br>neede</div>
<div class="node-label" style="left:403px;top:3196px">You pick your level<br>of involvement</div>
<div class="node-label" style="left:644px;top:3041px">This isn't theory.<br>This is practice.</div>
<div class="node-label" style="left:912px;top:2977px">You don't need large<br>checks to invest in<br>Venture Capital</div>

<div class="vline" style="left:600px;top:3420px;height:130px"></div>

<!-- CONTACT -->
<div class="contact-box"></div>
<h2 class="sec-title" style="top:3560px">Leave Us <span class="accent">a Message</span></h2>
<div class="field" style="left:272px;top:3649px;width:322px;height:43px"><svg viewBox="0 0 12 12"><circle cx="6" cy="4" r="3"/><path d="M0 12c0-4 3-5 6-5s6 1 6 5z"/></svg>First Name</div>
<div class="field" style="left:608px;top:3649px;width:320px;height:43px"><svg viewBox="0 0 12 12"><circle cx="6" cy="4" r="3"/><path d="M0 12c0-4 3-5 6-5s6 1 6 5z"/></svg>Last Name</div>
<div class="field" style="left:272px;top:3708px;width:322px;height:44px"><svg viewBox="0 0 12 12"><rect y="2" width="12" height="8"/></svg>Email address</div>
<div class="field" style="left:608px;top:3708px;width:320px;height:44px"><svg viewBox="0 0 12 12"><path d="M2 0l3 3-2 2c1 2 2 3 4 4l2-2 3 3-2 2C4 12 0 8 0 2z"/></svg>Phone Number</div>
<div class="field msg" style="left:272px;top:3769px;width:656px;height:92px"><svg viewBox="0 0 12 12"><ellipse cx="6" cy="5" rx="6" ry="4"/></svg>Message</div>
<a class="btn" style="left:495px;top:3878px;width:193px;height:43px;font-size:16px">Send Message →</a>

<!-- FOOTER -->
<div class="abs nav-logo" style="top:4088px"><div class="word">Moonlit</div><div class="sub">VENTURES</div></div>
<span class="social" style="left:127px"></span>
<span class="social" style="left:176px"></span>
<span class="social" style="left:224px"></span>
<span class="social" style="left:273px"></span>

<div class="foot-h" style="left:438px">Contact Us</div>
<svg class="abs" style="left:440px;top:4132px" width="18" height="18" viewBox="0 0 12 12" fill="#fff"><path d="M2 0l3 3-2 2c1 2 2 3 4 4l2-2 3 3-2 2C4 12 0 8 0 2z"/></svg>
<div class="foot-l" style="left:475px;top:4132px">555-014-2286</div>
<svg class="abs" style="left:440px;top:4176px" width="18" height="14" viewBox="0 0 18 14" fill="#fff"><rect width="18" height="14" rx="1"/><path d="M0 1l9 7 9-7" stroke="#000" fill="none"/></svg>
<div class="foot-l" style="left:475px;top:4173px">hello@moonlitventures.example</div>
<svg class="abs" style="left:442px;top:4222px" width="14" height="20" viewBox="0 0 14 20" fill="#fff"><path d="M7 0a7 7 0 0 1 7 7c0 5-7 13-7 13S0 12 0 7a7 7 0 0 1 7-7z"/><circle cx="7" cy="7" r="2.5" fill="#000"/></svg>
<div class="foot-l" style="left:475px;top:4216px;font-size:14px;line-height:20px">418 Harlow Quay St<br>Brenmoor, CA 90417</div>

<div class="foot-h" style="left:698px">Navigation</div>
<div class="foot-l" style="left:698px;top:4132px">Solutions</div>
<div class="foot-l" style="left:698px;top:4160px">Vision</div>
<div class="foot-l" style="left:698px;top:4188px">Programs</div>
<div class="foot-l" style="left:698px;top:4217px">Blogs</div>
<div class="foot-l" style="left:698px;top:4244px">Join Us</div>

<div class="foot-h" style="left:925px">Resources</div>
<div class="foot-l" style="left:925px;top:4132px">Terms of Use</div>
<div class="foot-l" style="left:925px;top:4160px">Privacy Policy</div>
<div class="foot-l" style="left:925px;top:4188px">Sitemap</div>
<div class="foot-l" style="left:925px;top:4217px">Contact</div>

<div class="copyright">Copyright © 2025 Moonlit Ventures. All Right Reserved</div>
</body>
</html>
```